Stump Grinding sidewalk sign

I have an A-frame sign that has a 24" x 36" flat area for a vinyl sign to be applied to. the sign can also be applied to sheet metal and then screwed to the A-frame sign.
I have included a few pictures of my logo, the A-frame, and my business card.

Target Market(s)

Tree and stump industry

Font styles to use
Decorative

Requirements
Must have
• I would like my company name , logo, slogan, and phone number on the sign. Along with "Fully Insured" and "free Estimates".
The sign is black, and I would like bright colors such as safety green and/or neon yellow. Or possibly a florescent red?
Nice to have
• Some sort of background to break up the blank "solidness"

```html
<!DOCTYPE html>
<html lang="en">
<head>
<meta charset="utf-8">
<title>Marlo's Stump Grinding – Sidewalk Sign</title>
<link rel="stylesheet" href="https://fonts.googleapis.com/css2?family=Oswald:wght@700&family=Jost:wght@700&display=swap">
<style>
  :root {
    --sign-yellow: #fdd80a;
    --sign-black: #1a1a18;
    --sign-white: #ffffff;
    --badge-gold: #e7b21c;
    --photo-grass: #6f9a45;
    --photo-wood: #b89a72;
  }
  * { margin: 0; padding: 0; box-sizing: border-box; }
  html, body { width: 818px; height: 1200px; overflow: hidden; background: var(--sign-white); }
  .sign { position: relative; width: 818px; height: 1200px; }
  .sign-backdrop { position: absolute; inset: 0; }
  .brand-name, .brand-trade, .headline-main, .headline-sub,
  .slogan, .perk, .phone-number { position: absolute; white-space: nowrap; }
  .brand-name {
    left: 58px; top: 34px;
    font-family: "Oswald", sans-serif; font-weight: 700;
    font-size: 104px; line-height: 1; letter-spacing: 1px;
    color: var(--sign-black);
  }
  .brand-trade {
    left: 64px; top: 152px;
    font-family: "Oswald", sans-serif; font-weight: 700;
    font-size: 46px; line-height: 1; letter-spacing: 2px;
    color: var(--sign-black);
  }
  .headline-main {
    left: 66px; top: 282px;
    font-family: "Jost", sans-serif; font-weight: 700;
    font-size: 104px; line-height: 1; letter-spacing: 1px;
    color: var(--sign-yellow);
  }
  .headline-sub {
    left: 68px; top: 372px;
    font-family: "Jost", sans-serif; font-weight: 700;
    font-size: 66px; line-height: 1; letter-spacing: 1px;
    color: var(--sign-yellow);
  }
  .slogan {
    left: 36px; top: 912px;
    font-family: "Jost", sans-serif; font-weight: 700;
    font-size: 43px; line-height: 50px; letter-spacing: 1px;
    color: var(--sign-black);
  }
  .slogan-divider {
    position: absolute; left: 303px; top: 918px;
    width: 2px; height: 98px; background: var(--sign-black);
  }
  .perk {
    left: 330px;
    display: flex; align-items: center; gap: 10px;
    font-family: "Jost", sans-serif; font-weight: 700;
    font-size: 50px; line-height: 1; letter-spacing: 1px;
    color: var(--sign-black);
  }
  .perk svg { width: 40px; height: 40px; flex: none; }
  .perk-estimate { top: 906px; }
  .perk-insured { top: 966px; }
  .phone-icon { position: absolute; left: 108px; top: 1072px; width: 92px; height: 92px; }
  .phone-number {
    left: 234px; top: 1078px;
    font-family: "Jost", sans-serif; font-weight: 700;
    font-size: 70px; line-height: 80px; letter-spacing: 1px;
    color: var(--sign-white);
  }
</style>
</head>
<body>
<main class="sign">
  <svg class="sign-backdrop" viewBox="0 0 818 1200" width="818" height="1200">
    <defs>
      <linearGradient id="photoTone" x1="0" y1="0" x2="1" y2="1">
        <stop offset="0" stop-color="#8fb85c"/>
        <stop offset="0.55" stop-color="var(--photo-grass)"/>
        <stop offset="1" stop-color="var(--photo-wood)"/>
      </linearGradient>
    </defs>
    <rect class="field-yellow" x="16" y="14" width="784" height="1170" fill="var(--sign-yellow)"/>
    <polygon class="band-headline" points="16,216 800,288 800,552 16,444" fill="var(--sign-black)"/>
    <polygon class="photo-area" role="img" aria-label="Photo of a stump grinder on a lawn beside a pile of cut logs and a fresh stump"
             points="16,444 800,552 800,904 16,732" fill="url(#photoTone)"/>
    <polygon class="band-stripe" points="16,732 800,904 800,914 16,768" fill="var(--sign-black)"/>
    <circle class="brand-mark" cx="600" cy="140" r="72" fill="var(--sign-black)"/>
    <circle class="guarantee-badge" role="img" aria-label="Satisfaction guarantee seal" cx="144" cy="800" r="88" fill="var(--badge-gold)"/>
    <rect class="band-contact" x="16" y="1040" width="784" height="144" fill="var(--sign-black)"/>
  </svg>

  <h1 class="brand-name">MARLO'S</h1>
  <p class="brand-trade">STUMP GRINDING</p>

  <h2 class="headline-main">STUMP</h2>
  <p class="headline-sub">REMOVAL SERVICES</p>

  <p class="slogan">NO STUMP<br>TOLL PLUM</p>
  <div class="slogan-divider"></div>

  <p class="perk perk-estimate">
    <svg viewBox="0 0 40 40" aria-hidden="true"><path d="M4 22 L15 33 L36 8" fill="none" stroke="var(--sign-black)" stroke-width="7" stroke-linecap="round" stroke-linejoin="round"/></svg>
    FREE ESTIMATE
  </p>
  <p class="perk perk-insured">
    <svg viewBox="0 0 40 40" aria-hidden="true"><path d="M4 22 L15 33 L36 8" fill="none" stroke="var(--sign-black)" stroke-width="7" stroke-linecap="round" stroke-linejoin="round"/></svg>
    FULLY INSURED
  </p>

  <svg class="phone-icon" viewBox="0 0 92 92" aria-hidden="true">
    <circle cx="46" cy="46" r="42" fill="none" stroke="var(--sign-white)" stroke-width="5"/>
    <path d="M33 24 c3 -2 6 -1 7 2 l4 9 c1 3 0 5 -2 6 l-3 2 c2 6 7 11 13 14 l2 -3 c2 -2 4 -2 6 -1 l9 4 c3 1 4 4 2 7 l-3 4 c-3 3 -8 4 -13 2 c-12 -5 -22 -15 -27 -27 c-2 -5 -1 -10 2 -13 z" fill="var(--sign-white)"/>
  </svg>
  <p class="phone-number">(555) 203 4418</p>
</main>
</body>
</html>
```